Masonry and Landscaping Construction company business card

Looking for a business card design for a construction company named Ferrante Construction. It is an italian-american family business that specializes in custom stone work, patios, walkways, driveways, steps, outdoor kitchens, concrete, waterproofing, power wash, landscaping and more. Our colors are mostly red and white with some black. We're looking for a bold design. we also like to incorporate a picture of my family's hometown somewhere in it.
Target Market(s)
Luxury home owners
Industry/Entity Type
Construction
Contact Information for Business Card
Details includes should be bullet points mentioning the services provided. Custom Stone Work, Outdoor Kitchens, Fire Pits, Patios, Walkways, Steps, Concrete, Waterproofing, powerwash and landscaping
Requirements
Must have
- Would like a spot on the card for co-owners names, numbers and email to be listed also looking to add the QR code for an instagram page
Nice to have
- would like something bold, based around the colors red and white with black outlines or details

```html
<!DOCTYPE html>
<html lang="en">
<head>
<meta charset="utf-8">
<title>Ferrante Construction – Business Card</title>
<link rel="stylesheet" href="https://fonts.googleapis.com/css2?family=Roboto+Condensed:wght@400;700&family=Roboto:wght@400;500&display=swap">
<style>
  :root {
    --backdrop: #3a3a3a;
    --card-white: #ffffff;
    --brand-red: #d71920;
    --brand-black: #1e1e1e;
    --band-grey: #2b2b2b;
    --service-green: #12d45c;
    --text-dark: #2a2a2a;
    --text-muted: #6d6d6d;
    --rule: #d0d0d0;
    --sky: #c9d3dc;
    --hills: #5f7a4a;
    --stone: #9b8a72;
  }
  * { margin: 0; padding: 0; box-sizing: border-box; }
  html, body { width: 1200px; height: 689px; overflow: hidden; }
  body {
    background: var(--backdrop);
    font-family: "Roboto", Arial, sans-serif;
    position: relative;
  }
  .card {
    position: absolute;
    top: 190px;
    width: 540px;
    height: 309px;
    border-radius: 18px;
    overflow: hidden;
    box-shadow: 0 12px 30px rgba(0,0,0,.45);
  }

  /* Front */
  .card-front { left: 40px; }
  .hometown-photo {
    position: absolute; inset: 0;
    background: linear-gradient(180deg, var(--sky) 0%, #aab9a0 30%, var(--hills) 55%, var(--stone) 80%, #6c7a52 100%);
  }
  .front-brand {
    position: absolute; top: 34px; right: 34px;
    display: flex; align-items: center; gap: 10px;
    font-family: "Roboto Condensed", Arial, sans-serif;
    font-weight: 700; font-size: 26px; line-height: 1.05;
    color: var(--brand-red); text-transform: uppercase; text-align: right;
  }
  .brand-mark { width: 16px; height: 16px; background: var(--brand-red); flex: none; }
  .services-band {
    position: absolute; left: 0; right: 0; top: 182px; height: 86px;
    background: var(--service-green);
    display: flex; flex-direction: column; justify-content: center; align-items: center;
    gap: 6px;
    font-family: "Roboto Condensed", Arial, sans-serif;
    font-size: 17px; color: var(--brand-black);
  }
  .service-line span + span::before {
    content: "•"; color: var(--brand-red); margin: 0 8px;
  }

  /* Back */
  .card-back { left: 620px; background: var(--card-white); }
  .back-brand {
    position: absolute; top: 40px; right: 30px;
    display: flex; align-items: center; gap: 10px;
    font-family: "Roboto Condensed", Arial, sans-serif;
    font-weight: 700; font-size: 26px; line-height: 1.05;
    color: var(--brand-red); text-transform: uppercase; text-align: right;
  }
  .divider {
    position: absolute; left: 190px; right: 30px; top: 122px;
    border-top: 1px solid var(--rule);
  }
  .address {
    position: absolute; right: 30px; top: 134px;
    text-align: right; font-size: 15px; line-height: 1.35; color: var(--text-dark);
  }
  .person { position: absolute; left: 30px; top: 166px; }
  .person-name {
    font-family: "Roboto Condensed", Arial, sans-serif;
    font-weight: 700; font-size: 24px; color: var(--brand-red);
    text-transform: uppercase; line-height: 1;
  }
  .person-role { font-size: 13px; color: var(--text-muted); margin-top: 2px; }
  .contact-list { list-style: none; margin-top: 8px; }
  .contact-list li {
    display: flex; align-items: center; gap: 8px;
    font-size: 14px; color: var(--text-dark); line-height: 1.45;
  }
  .contact-list svg { width: 12px; height: 12px; flex: none; }
  .footer-band { position: absolute; left: 0; bottom: 0; width: 540px; height: 50px; }
  .website {
    position: absolute; right: 24px; bottom: 20px;
    font-size: 13px; color: var(--card-white); letter-spacing: .3px;
  }
</style>
</head>
<body>

<section class="card card-front" aria-label="Card front">
  <div class="hometown-photo" role="img" aria-label="Photograph of the family's Italian hometown: stone church bell tower and houses on green mountain slopes under a cloudy sky"></div>
  <div class="front-brand">
    <span class="brand-mark"></span>
    <span>Ferrante<br>Construction</span>
  </div>
  <div class="services-band">
    <p class="service-line"><span>Custom Stone Work</span><span>Outdoor Kitchens</span><span>Fire Pits</span><span>Patios</span><span>Walkways</span></p>
    <p class="service-line"><span>Steps</span><span>Concrete</span><span>Waterproofing</span><span>Powerwash &amp; Landscaping</span></p>
  </div>
</section>

<section class="card card-back" aria-label="Card back">
  <div class="back-brand">
    <span class="brand-mark"></span>
    <span>Ferrante<br>Construction</span>
  </div>
  <div class="divider"></div>
  <p class="address">412 Orchard Row<br>Millbrook, Canada 20415</p>

  <div class="person">
    <p class="person-name">Marco Ferrante</p>
    <p class="person-role">President</p>
    <ul class="contact-list">
      <li><svg viewBox="0 0 12 12"><path d="M2 1 L4.5 1 L5 4 L3.6 4.8 Q4.6 7.2 7.2 8.4 L8 7 L11 7.5 L11 10 Q6 11 3 7.5 Q1 5 2 1Z" fill="var(--brand-red)"/></svg>555-014-3254</li>
      <li><svg viewBox="0 0 12 12"><rect x="3" y="0.8" width="6" height="10.4" rx="1" fill="none" stroke="var(--brand-red)" stroke-width="1.3"/></svg>555-016-3654</li>
      <li><svg viewBox="0 0 12 12"><rect x="0.8" y="2.5" width="10.4" height="7" fill="var(--brand-red)"/><path d="M1 3 L6 7 L11 3" fill="none" stroke="#fff" stroke-width="1"/></svg>info@ferranteconstruction.com</li>
    </ul>
  </div>

  <svg class="footer-band" viewBox="0 0 540 50" preserveAspectRatio="none" aria-hidden="true">
    <polygon points="0,44 300,44 326,4 540,4 540,50 0,50" fill="var(--band-grey)"/>
    <polygon points="0,34 290,34 312,6 322,6 298,40 0,40" fill="var(--brand-red)"/>
  </svg>
  <p class="website">www.ferranteconstruction.com</p>
</section>

</body>
</html>
```